依頼詳細
PCサイトを応募いただき、コンペ決定後、スマホサイトのデザインをお願いしたいと思います。
ただ、レスポンシブで考えているので、あまり複雑な構造にはしたくないと思っています。このあたりが分かる方からデザインをお願いします。
ページ数
1ページ
希望イメージ
シンプル 複雑
単色 カラフル
暗い 明るい
日常 高級
遊び心 厳粛
未来的 伝統的
女性的 男性的
希望する色
緑系、青系
納品ファイル
• イラストレーター形式 (.ai)
• フォトショップ形式 (.psd)
• PNG形式 (.png)
補足説明
ふぁきる形式はいずれか1つ。アウトラインありとなしで納品をお願いします。
■ 選んだ理由

クライアントのイメージ通りでした。

■ 提案者全員のお礼・コメント

たくさんのご提案ありがとうございました。
次回もぜひ、よろしくお願い致します。

```html
<!DOCTYPE html>
<html lang="ja">
<head>
<meta charset="utf-8">
<title>青柳屋 ユキドーム</title>
<link href="https://fonts.googleapis.com/css2?family=Noto+Sans+JP:wght@400;700;900&family=Noto+Serif+JP:wght@500;700&family=M+PLUS+1p:wght@800&display=swap" rel="stylesheet">
<style>
:root{
  --blue:#1f8fd6;
  --blue-dark:#0f6fb0;
  --sky:#cfe6f6;
  --ink:#222;
  --gray:#555;
  --band:#5a5a5a;
  --foot:#1e9bd7;
  --foot-dark:#222;
  --white:#fff;
}
*{margin:0;padding:0;box-sizing:border-box}
html,body{width:1200px;height:4320px;overflow:hidden}
body{font-family:"Noto Sans JP",sans-serif;color:var(--ink);background:var(--white);position:relative}
.pattern{background:var(--sky);background-image:radial-gradient(rgba(255,255,255,.45) 2px,transparent 2px);background-size:14px 14px}

.hero{position:absolute;top:0;left:0;width:1200px;height:820px;background:linear-gradient(180deg,#6b9fd0 0%,#a9c9e6 40%,#e9eef3 62%,#8a8f8c 82%,#5d6260 100%)}
.site-header{position:absolute;top:0;left:0;width:1200px;height:58px;background:rgba(20,40,70,.75);color:var(--white);display:flex;align-items:center;padding:0 250px}
.brand{display:flex;align-items:center;gap:10px;font-size:26px;font-weight:700}
.brand small{font-size:11px;font-weight:400;margin-left:10px;opacity:.9}
.header-contact{margin-left:auto;display:flex;align-items:center;gap:16px;font-size:11px;line-height:1.4}
.header-contact .tel{font-size:26px;font-weight:700}
.hero-copy{position:absolute;top:140px;width:100%;text-align:center}
.hero-copy .lead{font-size:30px;font-weight:700;color:#0d2a4a;letter-spacing:2px}
.hero-copy .name{font-family:"M PLUS 1p",sans-serif;font-size:120px;font-weight:800;color:var(--blue);font-style:italic;letter-spacing:14px;line-height:1.2;text-shadow:0 0 10px #fff,0 0 4px #fff}

.features{position:absolute;top:820px;left:0;width:1200px;height:560px}
.sec-lead{position:absolute;top:56px;left:0;width:100%;text-align:center;font-size:27px;font-weight:700;color:var(--ink)}
.sec-lead::after{content:"";display:block;width:980px;height:3px;margin:14px auto 0;background:var(--blue)}
.feature-list{position:absolute;top:170px;left:110px;width:980px;display:flex;justify-content:space-between}
.feature{width:300px;text-align:center;font-size:17px;font-weight:700}
.feature .photo{margin-top:20px;height:250px}

.voice{position:absolute;top:1380px;left:0;width:1200px;height:860px}
.sec-title{text-align:center;font-family:"Noto Serif JP",serif;font-size:44px;font-weight:700;color:var(--ink)}
.voice .sec-title{position:absolute;top:120px;width:100%;display:flex;justify-content:center;align-items:center;gap:12px}
.voice-list{position:absolute;top:270px;left:140px;width:920px;display:flex;justify-content:space-between}
.voice-item{width:420px}
.voice-item h3{font-family:"Noto Serif JP",serif;font-size:22px;font-weight:700;text-align:center;line-height:1.5;height:100px}
.voice-item .photo{height:200px;margin-bottom:18px}
.voice-item p{font-size:14px;line-height:1.9;text-align:center}
.voice-item .who{margin-top:14px;font-size:13px;color:var(--gray)}

.truck-mark{position:absolute;top:2300px;left:575px}
.size{position:absolute;top:2380px;left:0;width:1200px;height:660px}
.size .sec-title{position:absolute;top:60px;width:100%;font-family:"M PLUS 1p",sans-serif;font-style:italic;color:var(--blue);font-size:56px;letter-spacing:8px}
.size .intro{position:absolute;top:170px;width:100%;text-align:center;font-family:"Noto Serif JP",serif;font-size:24px;line-height:1.8}
.size-list{position:absolute;top:320px;left:200px;width:800px;display:flex;justify-content:space-between}
.size-item{width:220px;text-align:center}
.size-item .letter{font-family:"M PLUS 1p",sans-serif;font-size:48px;font-weight:800;color:var(--blue-dark)}
.size-item .desc{font-size:15px;font-weight:700;margin-top:14px}
.size-item .price{font-family:"Noto Serif JP",serif;font-size:34px;font-weight:700}
.size-item .note{font-size:13px;font-weight:700}

.contact{position:absolute;top:3040px;left:0;width:1200px;height:120px;background:var(--band);color:var(--white);display:flex;justify-content:center;align-items:center;gap:100px;font-size:30px;letter-spacing:3px}
.contact .tel{font-size:34px;letter-spacing:6px}

.access{position:absolute;top:3160px;left:0;width:1200px;height:660px}
.access .sec-title{position:absolute;top:90px;width:100%;display:flex;justify-content:center;align-items:center;gap:12px}
.access .addr{position:absolute;top:180px;width:100%;text-align:center;font-size:14px}
.access .map{position:absolute;top:240px;left:250px;width:700px;height:320px}

.site-footer{position:absolute;top:3820px;left:0;width:1200px;height:430px;background:var(--foot);color:var(--white)}
.foot-nav{position:absolute;top:40px;left:90px;width:1020px;display:flex;justify-content:space-between;font-size:15px;line-height:1.9}
.foot-nav ul{list-style:none;width:230px}
.copy{position:absolute;top:4250px;left:0;width:1200px;height:70px;background:var(--foot-dark);color:#ddd;font-size:12px;display:flex;align-items:center;justify-content:center}
</style>
</head>
<body>

<section class="hero">
  <div role="img" aria-label="雪空の下に建つ白いトラック用ビニールハウスガレージの写真" style="position:absolute;inset:0"></div>
  <header class="site-header">
    <div class="brand"><svg width="22" height="22"><circle cx="11" cy="11" r="9" fill="#fff"/></svg>青柳屋<small>農業用ハウス専門店</small></div>
    <div class="header-contact">
      <span>お問い合わせ先<br>こちら</span>
      <svg width="22" height="22" viewBox="0 0 24 24"><path fill="#fff" d="M6.6 10.8a15 15 0 0 0 6.6 6.6l2.2-2.2c.3-.3.7-.4 1-.2 1.1.4 2.3.6 3.6.6.6 0 1 .4 1 1V20c0 .6-.4 1-1 1A17 17 0 0 1 3 4c0-.6.4-1 1-1h3.5c.6 0 1 .4 1 1 0 1.3.2 2.5.6 3.6.1.3 0 .7-.2 1z"/></svg>
      <span><span class="tel">025-000-4410</span><br>info@aoyagiya.example.jp</span>
    </div>
  </header>
  <div class="hero-copy">
    <p class="lead">雪国発・トラック用ビニールハウスガレージ</p>
    <h1 class="name">ユキドーム</h1>
  </div>
</section>

<section class="features pattern">
  <h2 class="sec-lead">ビニールハウスの技術から生まれたコスパ抜群のトラック用ガレージ</h2>
  <div class="feature-list">
    <div class="feature">プレハブ式より低コストでお手軽<div class="photo" role="img" aria-label="ガレージ前に停めた赤いトラクターの写真" style="background:linear-gradient(#dfe4e8,#b35a4a 70%,#8d8f8a)"></div></div>
    <div class="feature">雪や風に強い超硬丈夫パイプを使用<div class="photo" role="img" aria-label="ガレージ内部のパイプ骨組みの写真" style="background:linear-gradient(#f4f6f6,#c9cfcf 60%,#7d7a70)"></div></div>
    <div class="feature">ガレージ以外にも組織使える<div class="photo" role="img" aria-label="畑作りに使うガレージ内部の写真" style="background:linear-gradient(#eef0ef,#b8b1a0 60%,#8b7c64)"></div></div>
  </div>
</section>

<section class="voice">
  <h2 class="sec-title">お客様の声 &gt;<svg width="40" height="40"><circle cx="20" cy="20" r="16" fill="#333"/></svg></h2>
  <div class="voice-list">
    <article class="voice-item">
      <h3>広くて明るい庫内<br>日中は照明不要</h3>
      <div class="photo" role="img" aria-label="明るい庫内に農機が並ぶ写真" style="background:linear-gradient(#e8ecee,#a9a59c 60%,#b44a3a)"></div>
      <p>「広い、安い、明るい」当社に来られたお客様に<br>ユキドームを見て頂くことが一番の宣伝になります。<br>庫内は非常に明るく、日中は照明不要で<br>使用できます。</p>
      <p class="who">新潟市　T社様</p>
    </article>
    <article class="voice-item">
      <h3>少ない除雪回数で済みます</h3>
      <div class="photo" role="img" aria-label="雪に囲まれたガレージの写真" style="background:linear-gradient(#c9d7e6,#f2f4f6 55%,#dfe3e8)"></div>
      <p>トラクター・コンバインの格納に使用。<br>5年が過ぎました。大雪の年も丈夫で<br>従来のビニールハウスに比べ、除雪回数が格段に<br>少なくて済みます。とにかく雪に強いです。</p>
      <p class="who">長岡市　S様</p>
    </article>
  </div>
</section>

<svg class="truck-mark" width="50" height="40" viewBox="0 0 50 40"><rect x="0" y="6" width="30" height="22" fill="#333"/><path d="M31 12h11l7 9v7H31z" fill="#333"/><circle cx="10" cy="32" r="5" fill="#333"/><circle cx="40" cy="32" r="5" fill="#333"/></svg>

<section class="size pattern">
  <h2 class="sec-title">サイズ</h2>
  <p class="intro">3サイズから選べます。<br>※その他のサイズもオーダー可能です。</p>
  <div class="size-list">
    <div class="size-item"><div class="letter">S</div><svg width="150" height="60"><path d="M5 58V30Q75-10 145 30v28z" fill="#1f8fd6"/></svg><p class="desc">小型トラック1台程度の広さ</p><p class="price">90万円</p><p class="note">本体・工事費込み</p></div>
    <div class="size-item"><div class="letter">M</div><svg width="180" height="60"><path d="M5 58V30Q90-10 175 30v28z" fill="#1f8fd6"/></svg><p class="desc">中型トラック1台程度の広さ</p><p class="price">170万円</p><p class="note">本体・工事費込み</p></div>
    <div class="size-item"><div class="letter">L</div><svg width="210" height="60"><path d="M5 58V30Q105-10 205 30v28z" fill="#1f8fd6"/></svg><p class="desc">大型トラック1台程度の広さ</p><p class="price">210万円</p><p class="note">本体・工事費込み</p></div>
  </div>
</section>

<section class="contact"><span>お問い合わせ</span><span class="tel">0120-00-4410</span></section>

<section class="access">
  <h2 class="sec-title"><svg width="40" height="40"><circle cx="20" cy="20" r="16" fill="#333"/></svg>アクセス</h2>
  <p class="addr">本社：〒950-0000　新潟県新潟市東区みなと町2-4-6</p>
  <div class="map" role="img" aria-label="本社周辺の地図" style="background:linear-gradient(135deg,#e9eef0,#d7e6d4 50%,#a9cfe8)"></div>
</section>

<footer class="site-footer">
  <nav class="foot-nav">
    <ul><li>パイプ・ビニールハウス</li><li>大型ハウス</li><li>園芸用</li><li>耐雪・農舎用</li><li>パイプハウス</li><li>育苗用ハウス</li><li>イチゴ用ハウス</li></ul>
    <ul><li>飲食ハウス</li><li>鉄骨ハウス</li><li>メンテナンス</li><li>フィルム張替</li><li>補強工事用</li><li>資材施設・設備品</li></ul>
    <ul><li>農業土壌</li><li>ミナモアグリ（土壌改良）</li><li>その他</li><li>農業用ビニール加工</li><li>当社資材</li><li>防虫網（市販）</li><li>ガーデン部</li><li>ドーム</li></ul>
    <ul><li>会社案内</li><li>採用情報</li><li>お問い合わせ</li></ul>
  </nav>
</footer>
<div class="copy">Copyright © 2000-2020 株式会社青柳屋　本ウェブサイトに掲載されている画像等の無断転載はご遠慮ください</div>

</body>
</html>
```